Halvorn spray foam and Environmental

I have business cards but need new ones. The ones I have are very bland. Here is. Y company website http://www.halvornsprayfoam.ca

Also I can send you copies of the current cards
I would also need my current logo on the new design as well.. Also spray foam and Environmental

Industry/Entity Type

Business

Logo Text

Halvorn.

```html
<!DOCTYPE html>
<html lang="en">
<head>
<meta charset="utf-8">
<title>Halvorn Spray Foam and Environmental – Business Cards</title>
<link rel="stylesheet" href="https://fonts.googleapis.com/css2?family=Montserrat:wght@700&family=Arimo:wght@400&display=swap">
<style>
  :root {
    --page: #ffffff;
    --card: #ffffff;
    --accent: #5a2d8f;
    --heading: #1f6b3b;
    --ink: #2f2f2f;
    --divider: #5a5a5a;
    --block: #4a4a4c;
  }
  * { box-sizing: border-box; margin: 0; padding: 0; }
  html, body {
    width: 950px; height: 1200px; overflow: hidden;
    background: var(--page);
  }
  .canvas { position: relative; width: 950px; height: 1200px; }
  .card {
    position: absolute; left: 48px; width: 833px; height: 475px;
    background: var(--card);
    box-shadow: 14px 14px 22px rgba(0,0,0,0.28);
  }
  .card--front { top: 66px; }
  .card--back { top: 595px; }

  .brand {
    position: absolute; left: 48px; top: 152px; width: 300px;
    display: flex; flex-direction: column; align-items: center;
  }
  .brand__square {
    width: 108px; height: 89px; background: var(--block);
  }
  .brand__name {
    margin-top: 16px;
    font-family: "Arimo", sans-serif; font-weight: 400;
    font-size: 42px; line-height: 50px;
    color: var(--ink);
  }
  .divider {
    position: absolute; left: 362px; top: 92px;
    width: 1.5px; height: 281px; background: var(--divider);
  }
  .info { position: absolute; left: 395px; top: 92px; }
  .section + .section { margin-top: 48px; }
  .section__title {
    font-family: "Montserrat", sans-serif; font-weight: 700;
    font-size: 22px; line-height: 30px; color: var(--heading);
    letter-spacing: 0.3px;
  }
  .section__line {
    display: flex; align-items: center; gap: 8px;
    font-family: "Arimo", sans-serif; font-size: 21px; line-height: 29px;
    color: var(--ink); white-space: nowrap;
  }
  .icon { width: 18px; height: 18px; flex: none; fill: var(--accent); }
</style>
</head>
<body>
<div class="canvas">

  <section class="card card--front" aria-label="Card front">
    <div class="brand">
      <div class="brand__square"></div>
      <div class="brand__name">Halvorn</div>
    </div>
    <div class="divider"></div>
    <div class="info">
      <div class="section">
        <h2 class="section__title">SPRAY FOAM</h2>
        <p class="section__line"><svg class="icon" viewBox="0 0 24 24"><path d="M6.6 10.8a15.1 15.1 0 0 0 6.6 6.6l2.2-2.2a1 1 0 0 1 1-.25 11.4 11.4 0 0 0 3.6.57 1 1 0 0 1 1 1V20a1 1 0 0 1-1 1A17 17 0 0 1 3 4a1 1 0 0 1 1-1h3.5a1 1 0 0 1 1 1c0 1.250.2 2.450.57 3.57a1 1 0 0 1-.25 1z"/></svg>604-555-0148</p>
        <p class="section__line"><svg class="icon" viewBox="0 0 24 24"><path d="M2 5h20v14H2z"/><path d="M2 5l10 8 10-8" fill="none" stroke="#fff" stroke-width="1.6"/></svg>halvornfoam@halvornsprayfoam.ca</p>
        <p class="section__line"><svg class="icon" viewBox="0 0 24 24"><circle cx="12" cy="12" r="9.5" fill="none" stroke="var(--accent)" stroke-width="1.8"/><path d="M2.5 12h19M12 2.5c3 3 3 16 0 19M12 2.5c-3 3-3 16 0 19M4.5 7h15M4.5 17h15" fill="none" stroke="var(--accent)" stroke-width="1.4"/></svg>www.halvornsprayfoam.ca</p>
      </div>
      <div class="section">
        <h2 class="section__title">ENVIRONMENTAL</h2>
        <p class="section__line"><svg class="icon" viewBox="0 0 24 24"><path d="M6.6 10.8a15.1 15.1 0 0 0 6.6 6.6l2.2-2.2a1 1 0 0 1 1-.25 11.4 11.4 0 0 0 3.6.57 1 1 0 0 1 1 1V20a1 1 0 0 1-1 1A17 17 0 0 1 3 4a1 1 0 0 1 1-1h3.5a1 1 0 0 1 1 1c0 1.250.2 2.450.57 3.57a1 1 0 0 1-.25 1z"/></svg>604-555-0172</p>
        <p class="section__line"><svg class="icon" viewBox="0 0 24 24"><path d="M2 5h20v14H2z"/><path d="M2 5l10 8 10-8" fill="none" stroke="#fff" stroke-width="1.6"/></svg>enviro1@halvornenvironmental.ca</p>
        <p class="section__line"><svg class="icon" viewBox="0 0 24 24"><circle cx="12" cy="12" r="9.5" fill="none" stroke="var(--accent)" stroke-width="1.8"/><path d="M2.5 12h19M12 2.5c3 3 3 16 0 19M12 2.5c-3 3-3 16 0 19M4.5 7h15M4.5 17h15" fill="none" stroke="var(--accent)" stroke-width="1.4"/></svg>www.halvornenvironmental.ca</p>
      </div>
    </div>
  </section>

  <section class="card card--back" aria-label="Card back">
    <div class="brand">
      <div class="brand__square"></div>
      <div class="brand__name">Halvorn</div>
    </div>
    <div class="divider"></div>
    <div class="info">
      <div class="section">
        <h2 class="section__title">SPRAY FOAM</h2>
        <p class="section__line">Roofing Foam, Slabjacking,</p>
        <p class="section__line">2 Pound / Half Pound, Attic Blow In,</p>
        <p class="section__line">Sound Proofing, Batt Insulation,</p>
      </div>
      <div class="section">
        <h2 class="section__title">ENVIRONMENTAL</h2>
        <p class="section__line">Air Monitoring, Asbestos Testing,</p>
        <p class="section__line">Asbestos Removal, Mould Removal,</p>
        <p class="section__line">Building Demolition, Lead Testing</p>
      </div>
    </div>
  </section>

</div>
</body>
</html>
```